Restaurant website built on Plinko’s responsive platform- No coding skills needed

We are looking to add to our company's website www.plinkoweb.example a new inspiration page that will include examples of sites built using Plinko's platform.
In order to make it relevant, we would like to have multiple choices for every category, one of the categories is “restaurants.”

REQUIREMENTS:
o Build a "fake" restaurant site on Plinko’s responsive platform, no real restaurant information is needed. The site will include:
1. Homepage
• Restaurant header (no logo)
• Paragraph about the restaurant (can be Lorem ipsum)
• Contact details and contact buttons
• Gribbo reviews
• Reserve-a-table widget
• Open hours
2. Menu page
• You can use any menu you'd like
• Reserve a table widget
• Photo gallery
3. Footer
• Social Media links
• Map with location of restaurant

* Order of the elements is up to the designer
* Designer may add more elements as they see fit
* Designer may alter elements from page to page
* Designer will define the site color pallet and text style

****Learn more on how to create a website on Plinko's platform here
https://clipvault.example/584736201

INSTRUCTIONS FOR THIS PROJECT:
Register for a 30-day free trial for Pro access to the platform:
http://www.plinkoweb.example/plinkopro?_dm_referral=ArtHvn

a. After registering, access the dashboard and click on “Create Responsive Website.”
b. Choose a template
c. Start editing! .
d. No need to publish. When ready, take a screenshot of the preview and submit the screenshot to this ArtHaven project. Include the URL/Link to the preview within the submission description.
e. For more information on Plinko, visit the support page at https://support.plinkoweb.example/02PlinkoOne/Quick_Guide OR call our Support line Mon.-Fri., 9AM-9PM ET.1-866-555-0147

DESIGN PREFERENCES
freestyle (not related to the Plinko brand)

DESIGN SAMPLES (for inspiration)
http://www.plinkoweb.example/responsive-website/templates

What not to include in the design -
no restrictions

DELIVERABLES:
* Website on Plinko (No PSD. No coding needed)
* Screenshot preview to ArtHaven with URL/link to your site’s preview.

ABOUT THE COMPANY:
Plinko is a website builder based in California that allow designers, web designers and practically anyone to build its own site. No development and/or technical skills required.

NOTE:
* Plinko is an external site and is not part of ArtHaven
* Please refer to Plinko's Terms and Conditions for information regarding how submissions will be handled (http://www.plinkoweb.example/legal/terms)

Target Market(s)

SMBs and web designers that want to create simple, professional and beautiful websites

Industry/Entity Type

Restaurant

Number of Pages Required

2 page

Requirements
Must have
• Please send a preview of the site you created on Plinko, NOT a PSD/JPEG
Should not have
• No coding skills are needed- any web designer can build a site on Plinko

```html
<!DOCTYPE html>
<html lang="en">
<head>
<meta charset="utf-8">
<title>Tablehouse</title>
<link href="https://fonts.googleapis.com/css2?family=Source+Sans+3:ital,wght@0,300;0,400;0,600;0,700;1,700&display=swap" rel="stylesheet">
<style>
:root{
  --red:#b10000;
  --ink:#333;
  --muted:#777;
  --white:#fff;
  --field:#e3e3e3;
  --night:#1d2631;
}
*{box-sizing:border-box;margin:0;padding:0}
html,body{width:695px;height:1200px;overflow:hidden}
body{position:relative;background:var(--white);font-family:"Source Sans 3",Arial,sans-serif;color:var(--ink)}
.abs{position:absolute}

/* hero */
.hero-photo{left:0;top:0;width:695px;height:310px;background:radial-gradient(ellipse at 55% 65%,#6b3a1f 0%,#a9764a 30%,#d9cbb8 60%,#ece6dd 100%)}
.topbar{left:0;top:0;width:695px;height:20px;background:rgba(90,90,90,.55)}
.topbar .social{left:487px;top:6px;display:flex;gap:5px}
.topbar .social span{width:7px;height:7px;border-radius:50%;background:var(--white)}
.header{left:0;top:20px;width:695px;height:59px;background:rgba(255,255,255,.72)}
.brand{left:0;top:38px;width:695px;text-align:center;font-size:18px;font-weight:700;color:var(--red);line-height:20px;letter-spacing:.3px}
.nav{left:0;top:79px;width:695px;height:21px;background:var(--red);display:flex;justify-content:center;align-items:center;gap:23px}
.nav a{color:var(--white);font-size:7px;text-decoration:none;text-transform:uppercase;letter-spacing:.3px;white-space:nowrap}
.hero-title{left:0;top:146px;width:695px;text-align:center;color:var(--white);text-transform:uppercase;font-weight:300}
.hero-title .small{display:block;font-size:24px;line-height:26px;letter-spacing:1px}
.hero-title .big{display:block;font-size:34px;line-height:36px;letter-spacing:.5px}
.btn{display:flex;align-items:center;justify-content:center;background:var(--red);color:var(--white);text-transform:uppercase;text-decoration:none;white-space:nowrap}
.order{left:286px;top:226px;width:125px;height:25px;font-size:11px;box-shadow:0 2px 3px rgba(0,0,0,.3)}

/* about */
.about-title{left:173px;top:340px;font-size:11px;font-weight:400;color:var(--red);text-transform:uppercase}
.about-text{left:172px;top:364px;width:168px;font-size:5.6px;line-height:8.5px;color:var(--muted)}
.read-more{left:171px;top:401px;width:102px;height:19px;font-size:7px}
.collage{left:352px;top:336px;width:169px;height:85px;background:linear-gradient(90deg,#5b4a3a,#8aa03a 30%,#c9c9c9 55%,#3b4a7a 75%,#2a3f6a)}

/* section bands */
.band{left:0;width:695px;height:31px;background:var(--red);color:var(--white);text-align:center;font-size:18px;line-height:31px;font-weight:300;text-transform:uppercase}
.band b{font-weight:700;font-style:italic}

/* reserve */
.reserve-bg{left:0;top:471px;width:695px;height:114px;background:linear-gradient(180deg,#26303c,var(--night))}
.field{top:512px;width:106px;height:15px;background:var(--field);font-size:6px;color:#555;padding:4px 5px;line-height:7px}
.field.select::after{content:"▾";position:absolute;right:3px;top:3px;font-size:6px}
.book{left:414px;top:535px;width:103px;height:16px;font-size:6.5px}

/* gallery */
.gallery{left:0;top:616px;width:695px;height:134px;display:flex;gap:1px;background:var(--white)}
.gallery div{flex:1}
.g1{background:radial-gradient(circle at 50% 30%,#e6a040,#6a1a0a 70%,#2a0a05)}
.g2{background:linear-gradient(180deg,#1a1a10,#6a8a20 55%,#4a7a1a)}
.g3{background:radial-gradient(ellipse at 50% 55%,#c98a3a,#7a9a3a 45%,#2a1a10 80%)}
.g4{background:radial-gradient(ellipse at 45% 60%,#e3b070,#c8d8b0 55%,#f0f0ea)}
.g5{background:linear-gradient(135deg,#8ab020,#a6c83a 60%,#5a8a10)}

/* hours */
.open-sign{left:173px;top:778px;width:107px;height:54px;background:linear-gradient(180deg,#d31a1a,#a00000);border-radius:3px}
.hours-title{left:173px;top:852px;font-size:13px;font-weight:400;color:var(--red)}
.hours{left:173px;top:878px;width:107px;font-size:5.6px;color:#555;border-collapse:collapse}
.hours td{padding:2px 0;white-space:nowrap}
.hours td:last-child{text-align:right}

/* reviews */
.review-tab{left:296px;top:779px;width:145px;height:24px;background:var(--red);color:var(--white);display:flex;align-items:center;gap:10px;padding-left:10px;font-size:8px;white-space:nowrap}
.review-tab .src{font-weight:700;font-size:9px}
.src-line{left:296px;top:812px;font-size:6px;font-weight:700;color:var(--red)}
.review{left:296px;width:228px;height:44px}
.review .avatar{position:absolute;left:0;top:0;width:36px;height:36px;background:linear-gradient(135deg,#caa080,#7a5a40)}
.review .who{position:absolute;left:44px;top:0;font-size:5.8px;color:#555;white-space:nowrap}
.review .who span{margin-left:10px}
.review .stars{position:absolute;left:44px;top:9px;display:flex;gap:1px}
.review .stars i{width:5px;height:5px;background:var(--red)}
.review p{position:absolute;left:44px;top:17px;width:184px;font-size:5.6px;line-height:7.5px;color:#555}
.reviews-rule{left:296px;top:935px;width:228px;height:1px;background:#999}
.more-link{left:296px;top:939px;font-size:5.6px;color:#1a5fa8;font-weight:600;white-space:nowrap}

/* map */
.map{left:0;top:992px;width:695px;height:175px;background:linear-gradient(100deg,#bcd3e8 0%,#e8e4da 20%,#efe9dc 50%,#a9c4df 62%,#eae5d8 75%,#e5e0d3 100%)}
.pin{left:282px;top:1064px}

/* footer */
.footer{left:0;top:1167px;width:695px;height:33px;background:var(--red)}
.foot-social{left:144px;top:1173px;display:flex;gap:2px}
.foot-social span{width:15px;height:15px;border:1.3px solid var(--white);border-radius:50%}
.copyright{left:0;top:1175px;width:695px;text-align:center;font-size:6px;color:var(--white);font-weight:600}
</style>
</head>
<body>

<div class="abs hero-photo" role="img" aria-label="Grilled steak and fried cutlet on a wooden board with sauce and a wine bottle"></div>
<div class="abs topbar">
  <div class="abs social"><span></span><span></span><span></span></div>
</div>
<div class="abs header"></div>
<div class="abs brand">TABLEHOUSE</div>
<nav class="abs nav">
  <a href="#">Welcome</a><a href="#">Our Stories</a><a href="#">Our Photos</a><a href="#">We Were Here</a><a href="#">By Me</a>
</nav>
<h1 class="abs hero-title"><span class="small">Consectetuer</span><span class="big">Adipiscing Elit</span></h1>
<a class="abs btn order" href="#">Order Now</a>

<h2 class="abs about-title">Who We Are</h2>
<p class="abs about-text">Lorem ipsum dolor sit amet, consectetuer adipiscing elit, sed diam nonummy nibh euismod tincidunt ut laoreet dolore magna aliquam erat volutpat. Ut wisi enim ad minim veniam,</p>
<a class="abs btn read-more" href="#">Read More</a>
<div class="abs collage" role="img" aria-label="Collage of dining room, table settings and staff photos"></div>

<h2 class="abs band" style="top:440px">Reserve a <b>Table</b></h2>
<div class="abs reserve-bg" role="img" aria-label="Dim restaurant dining room with chairs and glasses"></div>
<div class="abs field" style="left:177px">Date</div>
<div class="abs field" style="left:294px">Time</div>
<div class="abs field select" style="left:411px"></div>
<a class="abs btn book" href="#">Book Now</a>

<h2 class="abs band" style="top:585px">Photo <b>Gallery</b></h2>
<div class="abs gallery">
  <div class="g1" role="img" aria-label="Candlelit dining table"></div>
  <div class="g2" role="img" aria-label="Wine glasses on a green table setting"></div>
  <div class="g3" role="img" aria-label="Chicken burger with lettuce"></div>
  <div class="g4" role="img" aria-label="Seared fish fillet with herbs"></div>
  <div class="g5" role="img" aria-label="Fork on a green napkin"></div>
</div>

<div class="abs open-sign" role="img" aria-label="Hanging red open sign"></div>
<h3 class="abs hours-title">Working Hours</h3>
<table class="abs hours">
  <tr><td>Mon - Fri</td><td>9:00 am - 7:00 pm</td></tr>
  <tr><td>Saturday</td><td>10:00 am - 6:00 pm</td></tr>
  <tr><td>Sunday</td><td>Closed</td></tr>
</table>

<div class="abs review-tab"><span class="src">Gribbo</span><span>Real People . Real Reviews</span></div>
<div class="abs src-line">Gribbo</div>
<div class="abs review" style="top:831px">
  <div class="avatar" role="img" aria-label="Reviewer photo"></div>
  <div class="who">Marta K.<span>02/24/2015</span></div>
  <div class="stars"><i></i><i></i><i></i><i></i><i></i></div>
  <p>We came in knowing only what the Gribbo app had told us. A nearly perfect rating in a quiet old Italian block? I'm sold. I…<br><u>Read more</u></p>
</div>
<div class="abs review" style="top:884px">
  <div class="avatar" role="img" aria-label="Reviewer photo"></div>
  <div class="who">Dev R.<span>02/19/2015</span></div>
  <div class="stars"><i></i><i></i><i></i><i></i><i></i></div>
  <p>We had the tagliatelle with meat balls. Everything is great! Made fresh from scratch here, and it tastes just that, fresh!<br><u>Read more</u></p>
</div>
<div class="abs reviews-rule"></div>
<a class="abs more-link">Read more on Gribbo.com →</a>

<h2 class="abs band" style="top:960px">We<b>Were Here</b></h2>
<div class="abs map" role="img" aria-label="City street map showing the restaurant location"></div>
<svg class="abs pin" width="8" height="12" viewBox="0 0 8 12"><path d="M4 0a4 4 0 0 0-4 4c0 3 4 8 4 8s4-5 4-8a4 4 0 0 0-4-4z" fill="#d22"/><circle cx="4" cy="4" r="1.4" fill="#fff"/></svg>

<footer class="abs footer"></footer>
<div class="abs foot-social"><span></span><span></span><span></span><span></span><span></span></div>
<div class="abs copyright">Copyrights © 2015. Tablehouse.example</div>

</body>
</html>
```